Bright Oak Fitness Facility Business Cards

Business Card Design that incorporates the logo and tagline

Target Market(s)

Fitness, People Who Exercise

Contact Information for Business Card

2817 Mossgrove Bend Road
Tavares, Florida 32190
Phone: 352-555-Jump (5867)
www.brightoakfitness.example
info@brightoakfitness.example

Requirements
Must have
• Logo, Address, Website, email and tagline "Built For Better". Colors should be red/black/grey/white

```html
<!DOCTYPE html>
<html lang="en">
<head>
<meta charset="utf-8">
<title>Bright Oak Fitness – Business Card</title>
<link rel="stylesheet" href="https://fonts.googleapis.com/css2?family=Montserrat:wght@600&family=Open+Sans:wght@400&family=Playfair+Display:ital@1&display=swap">
<style>
  :root {
    --backdrop: #5a5a5a;
    --card-white: #ffffff;
    --brand-red: #ec1c24;
    --ink: #2a2a2a;
    --rule-grey: #b8b8b8;
  }
  * { margin: 0; padding: 0; box-sizing: border-box; }
  html, body { width: 1200px; height: 802px; overflow: hidden; }
  body { background: var(--backdrop); position: relative; font-family: "Open Sans", sans-serif; }

  .card {
    position: absolute;
    top: 274px;
    width: 442px;
    height: 264px;
    box-shadow: 0 3px 8px rgba(0,0,0,0.45);
  }
  .card--front { left: 136px; background: var(--card-white); }
  .card--back  { left: 624px; background: var(--brand-red); }

  .front__name {
    position: absolute;
    left: 20px;
    width: 192px;
    top: 102px;
    text-align: center;
    font-family: "Montserrat", sans-serif;
    font-weight: 600;
    color: var(--brand-red);
    font-size: 23px;
    line-height: 1.15;
    letter-spacing: -0.2px;
  }
  .front__divider {
    position: absolute;
    left: 218px;
    top: 88px;
    width: 1px;
    height: 93px;
    background: var(--rule-grey);
  }
  .contact {
    position: absolute;
    left: 236px;
    top: 87px;
    color: var(--ink);
    font-size: 13px;
    line-height: 16px;
    white-space: nowrap;
  }
  .contact__address { margin-bottom: 14px; }
  .contact__row { display: flex; align-items: center; gap: 3px; margin-left: -15px; }
  .contact__icon { width: 12px; height: 12px; flex: none; }

  .back__name {
    position: absolute;
    left: 0; right: 0;
    top: 106px;
    text-align: center;
    font-family: "Montserrat", sans-serif;
    font-weight: 600;
    color: var(--card-white);
    font-size: 32px;
    letter-spacing: -0.5px;
    white-space: nowrap;
  }
  .back__tagline {
    position: absolute;
    left: 0; right: 0;
    top: 162px;
    text-align: center;
    font-family: "Playfair Display", serif;
    font-style: italic;
    color: var(--card-white);
    font-size: 24px;
    white-space: nowrap;
  }
</style>
</head>
<body>

  <section class="card card--front">
    <div class="front__name">BRIGHT OAK<br>FITNESS</div>
    <div class="front__divider"></div>
    <div class="contact">
      <p class="contact__address">2817 Mossgrove Bend Road<br>Tavares, Florida 32190</p>
      <p class="contact__row">
        <svg class="contact__icon" viewBox="0 0 12 12" aria-hidden="true"><path d="M1 5c0-2 2-3 5-3s5 1 5 3l-2 1-1-1.5H4L3 6z M3 6.5h6l1 3.5H2z" fill="#ec1c24"/></svg>
        352-555-Jump (5867)
      </p>
      <p class="contact__row">
        <svg class="contact__icon" viewBox="0 0 12 12" aria-hidden="true"><rect x="1" y="3" width="10" height="7" fill="#ec1c24"/><path d="M1 3l5 4 5-4" stroke="#fff" fill="none" stroke-width="1"/></svg>
        info@brightoakfitness.example
      </p>
      <p class="contact__row">
        <svg class="contact__icon" viewBox="0 0 12 12" aria-hidden="true"><circle cx="6" cy="6" r="5" fill="#ec1c24"/><path d="M4 3c1 1 0 2 1 3s2 0 2 2M8 3c-1 1 0 2 1 2" stroke="#fff" fill="none" stroke-width="1"/></svg>
        www.brightoakfitness.example
      </p>
    </div>
  </section>

  <section class="card card--back" role="img" aria-label="Red card back with a faint repeating brand pattern">
    <div class="back__name">BRIGHT OAK FITNESS</div>
    <div class="back__tagline">Built For Better</div>
  </section>

</body>
</html>
```